Business Card- Occupational Therapist

I need business cards for Tallowood KinderMove, I am an Occupational Therapist offering child centred play therapy.
I am a sole private practitioner offering play therapy services to families in rural Great Southern region of WA, my mission statement is "helping rural children and communities thrive"
This is a new business so I am needing to promote the value of child centred play therapy within the community, and my referrers (target audience) will be: rural GPs (doctors), child health nurse, schools, disability providers, child protection workers etc) but also the families of young children in rural areas.
Target Market(s)
Families of children
Referrers (Doctors, child health nurse, schools, disability providers, child protection workers)
Industry/Entity Type
Mental Health
Contact Information for Business Card
Mira Toveland
Occupational Therapist
Phone: 0487 552 019
Email: mira@tkmove.com.au
PO Box 71 | BRINDLECOMBE WA 6412
Requirements
Must have
- Include Tallowood KinderMove logo and my contact details.
Include my credentials as an Occupational Therapist and Child Centred Play Therapist
Nice to have
- "Play is a child's language and toys are their words" Delbert Quorin

```html
<!DOCTYPE html>
<html lang="en">
<head>
<meta charset="utf-8">
<title>Tallowood KinderMove – Business Cards</title>
<link rel="stylesheet" href="https://fonts.googleapis.com/css2?family=Quicksand:wght@500;700&family=Arimo:wght@400;700&display=swap">
<style>
  :root {
    --page-bg: #d9d9d9;
    --purple: #6a1b63;
    --purple-mid: #5e2a5e;
    --green: #22a22f;
    --green-dark: #2f7a3c;
    --card-white: #f4f4f4;
    --ink: #1b1b1b;
    --rule: #b5b5b5;
    --white: #ffffff;
  }
  * { box-sizing: border-box; margin: 0; padding: 0; }
  html, body {
    width: 1200px; height: 900px; overflow: hidden;
    background: var(--page-bg);
  }
  .canvas { position: relative; width: 1200px; height: 900px; }

  .card {
    position: absolute;
    width: 640px; height: 370px;
    border-radius: 26px;
    overflow: hidden;
    box-shadow: 0 6px 18px rgba(0,0,0,.22);
  }

  /* Front card */
  .card-front {
    left: 120px; top: 50px;
    background: linear-gradient(200deg, var(--green) 0%, var(--green-dark) 28%, var(--purple-mid) 62%, var(--purple) 100%);
    color: var(--white);
  }
  .front-brand {
    position: absolute; left: 150px; top: 120px;
    display: flex; align-items: center; gap: 26px;
  }
  .brand-dot {
    display: block;
    width: 86px; height: 86px; border-radius: 50%;
    background: var(--white);
  }
  .brand-name {
    font-family: "Quicksand", sans-serif;
    font-weight: 500;
    font-size: 40px; line-height: 1.05;
    letter-spacing: .5px;
  }
  .front-quote {
    position: absolute; left: 0; right: 0; bottom: 58px;
    text-align: center;
    font-family: "Arimo", sans-serif;
    font-size: 17px; line-height: 1.45;
  }
  .front-quote .quote-author { display: block; font-weight: 700; font-size: 16px; }

  /* Back card */
  .card-back {
    left: 440px; top: 480px;
    background: var(--card-white);
  }
  .back-brand {
    position: absolute; left: 48px; top: 56px; width: 250px;
    text-align: center;
  }
  .back-brand .brand-name { color: var(--ink); font-size: 34px; }
  .back-brand .brand-dot {
    margin: 20px auto 0;
    width: 96px; height: 96px;
    background: var(--green);
  }
  .divider {
    position: absolute; left: 318px; top: 48px;
    width: 1px; height: 214px; background: var(--rule);
  }
  .contact {
    position: absolute; left: 342px; top: 50px; right: 20px;
    font-family: "Arimo", sans-serif; color: var(--ink);
  }
  .contact-name {
    font-family: "Quicksand", sans-serif; font-weight: 700;
    color: var(--green); font-size: 30px; line-height: 1.1;
  }
  .contact-role { font-size: 16px; line-height: 1.3; margin-top: 2px; }
  .contact-list { list-style: none; margin-top: 18px; font-size: 15px; line-height: 1.65; }
  .contact-list li { display: flex; align-items: center; gap: 8px; white-space: nowrap; }
  .contact-list svg { width: 20px; height: 16px; flex: none; }
  .contact-list .no-icon { padding-left: 28px; }
  .tagline-band {
    position: absolute; left: 0; right: 0; bottom: 0; height: 64px;
    background: var(--green);
    border-bottom: 12px solid var(--purple);
    display: flex; align-items: center; justify-content: center;
    font-family: "Arimo", sans-serif; color: var(--white);
    font-size: 21px; letter-spacing: .3px;
  }
</style>
</head>
<body>
<main class="canvas">

  <section class="card card-front" aria-label="Card front">
    <div class="front-brand">
      <span class="brand-dot" aria-hidden="true"></span>
      <p class="brand-name">Tallowood<br>KinderMove</p>
    </div>
    <p class="front-quote">"Play is a child's language and toys are their words"
      <span class="quote-author">-Delbert Quorin</span></p>
  </section>

  <section class="card card-back" aria-label="Card back">
    <div class="back-brand">
      <p class="brand-name">Tallowood<br>KinderMove</p>
      <span class="brand-dot" aria-hidden="true"></span>
    </div>
    <div class="divider" aria-hidden="true"></div>
    <div class="contact">
      <p class="contact-name">Mira Toveland</p>
      <p class="contact-role">Occupational Therapist<br>Play Therapist</p>
      <ul class="contact-list">
        <li class="no-icon">0487 552 019</li>
        <li>
          <svg viewBox="0 0 20 16" aria-hidden="true"><rect x="1" y="1" width="18" height="14" rx="1.5" fill="none" stroke="#22a22f" stroke-width="1.8"/><path d="M7 4c-1 0-2 1-1.6 2.6.6 2.4 2.6 4.6 5 5.2 1.5.4 2.6-.6 2.6-1.6l-1.8-1.2-1 1c-1.2-.5-2.2-1.5-2.6-2.6l1-1z" fill="#22a22f"/></svg>
          mira@tkmove.com.au
        </li>
        <li>
          <svg viewBox="0 0 20 16" aria-hidden="true"><rect x="1" y="2" width="18" height="12" fill="#22a22f"/><path d="M1 2l9 7 9-7" fill="none" stroke="#f4f4f4" stroke-width="1.5"/></svg>
          PO Box 71 BRINDLECOMBE WA 6412
        </li>
      </ul>
    </div>
    <div class="tagline-band">Supporting rural children and communities to thrive</div>
  </section>

</main>
</body>
</html>
```